Rate sheet redesign

We provide rate sheets to agents for our scenic flights and I would like to make them easier to read and more comprehensive. I'd also like to be able to edit the information in the design, as tours get updated and so do the rates. We've got new product out of shark bay, so the sections would need to be: Perth, Geraldton, Kalbarri and Shark Bay. I've attached what we've been using and also some concept photos.

also a link to our flights online: https://coralwingtours.bookvista.com/catalog/418752/flights-from-perth

I've put this under brochure redesign as I wasn't sure what a rate sheet would be considered. Open to different formats if it means content is editable.

Need extra days to review

```html
<!DOCTYPE html>
<html lang="en">
<head>
<meta charset="utf-8">
<title>Geraldton Rate Sheet 25/26</title>
<link href="https://fonts.googleapis.com/css2?family=Poppins:wght@400;500;600;700;800&display=swap" rel="stylesheet">
<style>
:root{
  --canvas:#e4e4e4;
  --navy:#0d2a8f;
  --royal:#0b5cf0;
  --deep:#0f1fa6;
  --orange:#f0921e;
  --ink:#2a2f3a;
  --cell:rgba(241,241,243,.96);
  --line:#c9ccd3;
  --sky-top:#dde9f4;
  --sky-mid:#8fb4d2;
  --sea:#1f5380;
}
*{box-sizing:border-box;margin:0;padding:0}
html,body{width:1064px;height:1200px;overflow:hidden}
body{background:var(--canvas);font-family:"Poppins",sans-serif;color:var(--ink);position:relative}

.page{position:absolute;width:473px;height:333px;overflow:hidden;box-shadow:0 6px 18px rgba(0,0,0,.18)}
.page--index{left:36px;top:43px}
.page--p2{left:540px;top:43px}
.page--p3{left:36px;top:410px}
.page--p4{left:540px;top:410px}
.page--p5{left:316px;top:790px}

.page__scene{position:absolute;inset:0;background:linear-gradient(180deg,var(--sky-top) 0%,#c2d7e9 22%,var(--sky-mid) 48%,#3d6f98 72%,var(--sea) 100%)}

.brand{position:absolute;left:22px;top:28px;display:flex;align-items:center;gap:5px}
.brand__dot{width:16px;height:16px;border-radius:50%;background:var(--orange)}
.brand__name{font-weight:600;font-size:10px;line-height:1.15;color:var(--navy)}

.title{position:absolute;left:118px;top:22px;font-weight:800;font-size:30px;line-height:1;color:var(--orange);white-space:nowrap}
.title__year{color:var(--navy)}
.page--index .title{top:36px}
.subtitle{position:absolute;left:121px;top:56px;font-weight:700;font-size:9.4px;color:var(--navy);white-space:nowrap}

.tab{position:absolute;left:133px;top:78px;width:208px;height:19px;background:var(--orange);border-radius:8px 8px 0 0;color:#fff;font-weight:700;font-size:10px;letter-spacing:5px;text-align:center;line-height:19px}

.rates{position:absolute;left:42px;top:96px;width:386px;border-radius:10px;overflow:hidden;background:var(--cell);border-collapse:separate;border-spacing:0;table-layout:fixed}
.rates th{height:28px;color:#fff;font-weight:500;font-size:11px}
.rates th:nth-child(odd){background:var(--royal)}
.rates th:nth-child(even){background:var(--deep)}
.rates th:nth-child(3){background:var(--deep)}
.rates td{font-size:4.5px;line-height:1.25;text-align:center;vertical-align:middle;padding:2px 4px;border-top:1px solid var(--line);border-right:1px solid var(--line)}
.rates td:last-child{border-right:0}
.rates td.price{font-weight:600;font-size:5px}
.pill{display:inline-block;color:#fff;font-weight:600;font-size:3.6px;padding:0 6px;border-radius:4px;line-height:5.5px;margin:1px 0}
.pill--included{background:var(--deep)}
.pill--duration{background:var(--orange)}

.index-table{position:absolute;left:42px;top:84px;width:387px;border-radius:10px;overflow:hidden;background:var(--cell);border-collapse:separate;border-spacing:0;table-layout:fixed}
.index-table th{height:28px;color:#fff;font-weight:500;font-size:11px}
.index-table th:nth-child(1){background:var(--royal)}
.index-table th:nth-child(2){background:var(--deep)}
.index-table th:nth-child(3){background:var(--deep)}
.index-table td{font-size:6px;line-height:1.3;text-align:center;vertical-align:middle;border-top:1px solid var(--line);border-right:1px solid var(--line)}
.index-table td:last-child{border-right:0}

.note{position:absolute;left:50px;right:50px;top:300px;font-size:4.4px;font-weight:700;color:#fff;text-align:center;line-height:1.4}
.page-num{position:absolute;right:22px;bottom:24px;width:10px;height:10px;border-radius:50%;border:1px solid #fff;color:#fff;font-size:4.5px;font-weight:600;text-align:center;line-height:8px}
</style>
</head>
<body>

<!-- Index page -->
<section class="page page--index">
  <div class="page__scene" role="img" aria-label="Aerial photo of reefs and ocean under a pale sky"></div>
  <div class="brand"><span class="brand__dot"></span><span class="brand__name">Coralwing<br>Aviation</span></div>
  <h1 class="title"><span class="title__year">25/26</span> RATES RETAIL</h1>
  <table class="index-table">
    <colgroup><col style="width:124px"><col style="width:140px"><col style="width:123px"></colgroup>
    <tr><th>Location</th><th>Address</th><th>Pages</th></tr>
    <tr style="height:26px"><td>Geraldton</td><td>14 Harbour View Rd, Eastcliff<br>WA 6532</td><td>2–5</td></tr>
    <tr style="height:38px"><td>Geraldton - Kalbarri<br>(only available to<br>Agents)</td><td>Departure dependant on Agent</td><td>6</td></tr>
    <tr style="height:28px"><td>Kalbarri</td><td>Hangar 3, Airfield Way, Kalbarri WA<br>6536</td><td>7–10</td></tr>
    <tr style="height:24px"><td>Perth</td><td>Southfield Airfield</td><td>11–13</td></tr>
    <tr style="height:26px"><td>Shark Bay</td><td>Airstrip Rd, Denham<br>WA 6537</td><td>14</td></tr>
    <tr style="height:24px"><td colspan="2">Terms and Conditions</td><td>15</td></tr>
  </table>
  <div class="page-num">01</div>
</section>

<!-- Page 2 -->
<section class="page page--p2">
  <div class="page__scene" role="img" aria-label="Aerial photo of coastline seen from an aircraft window"></div>
  <div class="brand"><span class="brand__dot"></span><span class="brand__name">Coralwing<br>Aviation</span></div>
  <h1 class="title">GERALDTON RATES</h1>
  <p class="subtitle">TOUR RATES VALID FROM 1ST APRIL 2025 TO 31ST MARCH 2026</p>
  <div class="tab">RETAIL RATES</div>
  <table class="rates">
    <colgroup><col style="width:91px"><col style="width:108px"><col style="width:70px"><col style="width:57px"><col style="width:60px"></colgroup>
    <tr><th>Flight</th><th>Inclusions</th><th>Clauses</th><th>Adult</th><th>Child</th></tr>
    <tr style="height:54px"><td>Abrolhos Island<br>Discovery Tour<br>(Flight 303)</td><td><span class="pill pill--included">Included</span><br>Scenic flight from Geraldton to East Wallabi Island return. Morning /Afternoon Tea, and snorkel gear.<br><span class="pill pill--duration">Duration</span><br>1 hour 20 minutes flight time<br>5 hours 30 minutes Total Tour time</td><td>Normal departure time is 8am, however timing is flexible depending on bookings. Start time must be 6 hours before sunset.</td><td class="price">$550.00</td><td class="price">$385.00</td></tr>
    <tr style="height:60px"><td>Abrolhos Island Discovery<br>Tour plus Pink Lake<br>(Flight 304)</td><td><span class="pill pill--included">Included</span><br>Scenic flight from Geraldton to East Wallabi Island return via Pink Lake. Morning /Afternoon Tea, and snorkel gear.<br><span class="pill pill--duration">Duration</span><br>2 hours flight time<br>6 hours Total Tour time</td><td>Normal departure time is 8am, however timing is flexible depending on bookings. Start time must be 6 hours before sunset.</td><td class="price">$610.00</td><td class="price">$427.00</td></tr>
    <tr style="height:54px"><td>Abrolhos Islands and<br>Batavia Shipwreck<br>(Flight 303B)</td><td><span class="pill pill--included">Included</span><br>Scenic flight from Geraldton to East Wallabi Island return, and Morning /Afternoon Tea.<br><span class="pill pill--duration">Duration</span><br>1 hour 20 minutes flight time<br>2 hours Total Tour time</td><td>Normal departure time is 2pm, however timing is flexible depending on bookings. Start time must be 2.5 hours before sunset.</td><td class="price">$500.00</td><td class="price">$350.00</td></tr>
  </table>
  <p class="note">PLEASE NOTE THERE IS A NEW $11 GOVERNMENT FEE FOR ALL FLIGHTS LANDING AT THE ABROLHOS ISLANDS, THIS IS NOT A COMMISSIONABLE FEE AND NEEDS TO BE PAID ON TOP OF THE NETT RATE</p>
  <div class="page-num">02</div>
</section>

<!-- Page 3 -->
<section class="page page--p3">
  <div class="page__scene" role="img" aria-label="Aerial photo of clouds over deep blue ocean"></div>
  <div class="brand"><span class="brand__dot"></span><span class="brand__name">Coralwing<br>Aviation</span></div>
  <h1 class="title">GERALDTON RATES</h1>
  <p class="subtitle">TOUR RATES VALID FROM 1ST APRIL 2025 TO 31ST MARCH 2026</p>
  <div class="tab">RETAIL RATES</div>
  <table class="rates">
    <colgroup><col style="width:91px"><col style="width:108px"><col style="width:70px"><col style="width:57px"><col style="width:60px"></colgroup>
    <tr><th>Flight</th><th>Inclusions</th><th>Clauses</th><th>Adult</th><th>Child</th></tr>
    <tr style="height:54px"><td>Abrolhos Islands<br>and Batavia<br>Shipwreck plus Pink Lake<br>(Flight 304B)</td><td><span class="pill pill--included">Included</span><br>Scenic flight from Geraldton to East Wallabi Island return via Pink Lake, and Morning /Afternoon Tea.<br><span class="pill pill--duration">Duration</span><br>2 hours flight time<br>2.5 hours Total Tour time</td><td>Normal departure time is 2pm, however timing is flexible depending on bookings. Start time must be 3 hours before sunset.</td><td class="price">$560.00</td><td class="price">$392.00</td></tr>
    <tr style="height:60px"><td>Ultimate Discovery Tour<br>(Abrol,Pink and Gorges)<br>(flight 305)</td><td><span class="pill pill--included">Included</span><br>Scenic flight from Geraldton to East-Wallabi Island return, including Kalbarri River Gorges and Pink Lake. Morning Tea/lunch, and snorkel gear.<br><span class="pill pill--duration">Duration</span><br>2 hour 15 minutes flight time<br>6 hours 30 minutes Total Tour time</td><td>Normal departure time is 8am, however timing is flexible depending on bookings. Start time must be 7 hours before sunset.</td><td class="price">$750.00</td><td class="price">$525.00</td></tr>
    <tr style="height:54px"><td>Grand Tour (Flight 306)</td><td><span class="pill pill--included">Included</span><br>Round flight from Geraldton of Kalbarri Town, Coastal Cliffs, River Gorges and Abrolhos Islands' Wallabi Group<br><span class="pill pill--duration">Duration</span><br>2 hours 15 minute Total Tour time</td><td>Normal departure time is 1:30pm, however timing is flexible depending on bookings. Start time must be 3 hours before sunset.</td><td class="price">$650.00</td><td class="price">$455.00</td></tr>
  </table>
  <p class="note">PLEASE NOTE THERE IS A NEW $11 GOVERNMENT FEE FOR ALL FLIGHTS LANDING AT THE ABROLHOS ISLANDS, THIS IS NOT A COMMISSIONABLE FEE AND NEEDS TO BE PAID ON TOP OF THE NETT RATE</p>
  <div class="page-num">03</div>
</section>

<!-- Page 4 -->
<section class="page page--p4">
  <div class="page__scene" role="img" aria-label="Aerial photo from an aircraft wing over the coast"></div>
  <div class="brand"><span class="brand__dot"></span><span class="brand__name">Coralwing<br>Aviation</span></div>
  <h1 class="title">GERALDTON RATES</h1>
  <p class="subtitle">TOUR RATES VALID FROM 1ST APRIL 2025 TO 31ST MARCH 2026</p>
  <div class="tab">RETAIL RATES</div>
  <table class="rates">
    <colgroup><col style="width:91px"><col style="width:108px"><col style="width:70px"><col style="width:57px"><col style="width:60px"></colgroup>
    <tr><th>Flight</th><th>Inclusions</th><th>Clauses</th><th>Adult</th><th>Child</th></tr>
    <tr style="height:52px"><td>Pink Lake Flight (Flight 307)</td><td><span class="pill pill--included">Included</span><br>Round flight of the Pink Lake from Geraldton.<br><span class="pill pill--duration">Duration</span><br>1 hour Total Tour time</td><td>Multiple times available for this flight, please request "Pink Lake schedule for full times list.</td><td class="price">$310.00</td><td class="price">$217.00</td></tr>
    <tr style="height:54px"><td>Pink Lake Flight plus Gorges<br>(Flight 308)</td><td><span class="pill pill--included">Included</span><br>Round flight of the Pink Lake and Kalbarri River Gorges from Geraldton.<br><span class="pill pill--duration">Duration</span><br>1 hour 40 minutes Total Tour time</td><td>Normal departure time is 3pm, however timing is flexible depending on bookings. Start time must be 2.5 hours before sunset.</td><td class="price">$500.00</td><td class="price">$350.00</td></tr>
    <tr style="height:78px"><td>Monkey Mia Dolphin<br>Spectacular with pink lake<br>(Flight 309)</td><td><span class="pill pill--included">Included</span><br>Scenic flight from Geraldton to Monkey Mia returning via the Pink Lake. Dolphin Feeding and nature cruise.<br><span class="pill pill--duration">Duration</span><br>3 hours flight time<br>8 hours Total Tour time</td><td>Monkey Mia dolphins are wild and in their natural environment, therefore sighting can't be guaranteed<br>Departure time is fixed due to ground activities. Not Available Christmas Day,New Years Day or February due to ground content being unavailable.</td><td class="price">$880.00</td><td class="price">$616.00</td></tr>
  </table>
  <div class="page-num">04</div>
</section>

<!-- Page 5 -->
<section class="page page--p5">
  <div class="page__scene" role="img" aria-label="Aerial photo of coastline and ocean under a light sky"></div>
  <div class="brand"><span class="brand__dot"></span><span class="brand__name">Coralwing<br>Aviation</span></div>
  <h1 class="title">GERALDTON RATES</h1>
  <p class="subtitle">TOUR RATES VALID FROM 1ST APRIL 2025 TO 31ST MARCH 2026</p>
  <div class="tab">RETAIL RATES</div>
  <table class="rates">
    <colgroup><col style="width:91px"><col style="width:108px"><col style="width:70px"><col style="width:57px"><col style="width:60px"></colgroup>
    <tr><th>Flight</th><th>Inclusions</th><th>Clauses</th><th>Adult</th><th>Child</th></tr>
    <tr style="height:54px"><td>Abrolhos Islands and Pink Lake<br>flyover (Flight 304C)</td><td><span class="pill pill--included">Included</span><br>Scenic flight from Geraldton to East Wallabi Island return via Pink Lake.<br><span class="pill pill--duration">Duration</span><br>2 hours Total Tour time</td><td>Normal departure time is 8am, however timing is flexible depending on bookings. Start time must be 2.5 hours before sunset.</td><td class="price">$600.00</td><td class="price">$420.00</td></tr>
    <tr style="height:56px"><td>Abrolhos Islands flyover<br>(Flight 303C)</td><td><span class="pill pill--included">Included</span><br>Scenic flight from Geraldton to East Wallabi Island return<br><span class="pill pill--duration">Duration</span><br>1 hours 30 minutes Total Tour time</td><td>Normal departure time is 8am, however timing is flexible depending on bookings. Start time must be 2 hours before sunset.</td><td class="price">$440.00</td><td class="price">$308.00</td></tr>
    <tr style="height:58px"><td>Geraldton Flyover<br>(Flight X)</td><td><span class="pill pill--included">Included</span><br>Scenic flight of the Geraldton area.<br><span class="pill pill--duration">Duration</span><br>30 minutes Total Tour time</td><td>Normal departure time is 8am, however timing is flexible depending on bookings. Start time must be 1 hour before sunset.</td><td class="price">$200.00</td><td class="price">$140.00</td></tr>
  </table>
  <p class="note">PLEASE NOTE THERE IS A NEW $11 GOVERNMENT FEE FOR ALL FLIGHTS LANDING AT THE ABROLHOS ISLANDS, THIS IS NOT A COMMISSIONABLE FEE AND NEEDS TO BE PAID ON TOP OF THE NETT RATE</p>
  <div class="page-num">05</div>
</section>

</body>
</html>
```